Emerging Education Provider Needs a Contemporary and Compelling Promotional Presentation

We are Juniper Learning and Skills Institute, a privately owned institution that is really going places. We offer a range of Diploma, Language and Short courses for both Domestic and International students with both face to face delivery and on-line or blended. We currently run out of two campuses in Brisbane (Queensland Australia) one in the heart of the city and one in the multi-cultural precinct of Bellhaven Rise. We are currently expanding with additional campuses planned for the Gold Coast and for Melbourne, Victoria.
Please refer to our web site jlsi-example.edu.au.
We need a promotional presentation (doesn't necessarily have to be in PowerPoint) to promote our business - It really needs to pop!
Proposed Pack:
Opening slide
Content & Agenda
CEO Welcome
Mission and Vision
Our Values
Why Choose JLSI (multiple slides)
Our Campuses (Brisbane, Bellhaven Rise, In Development)
Life in Brisbane (2 slides - Queensland and Brisbane)
Our Courses (3 slides - Domestic, International, On-Line)
Student Services (multiple slides)
How to Apply
Closing Slide
Updates

Reason: I will be travelling and unable to review submissions until early next week. Can all submissions please ensure the pack has a real wow factor. This will be a pack that we will have on a big screen at a trade show where thousands of people are walking by. The presentation needs to get people to stop and watch. So no graphs or data, few words per slide, lots of compelling images, a real contemporary feel.

Target Market(s)

Educational institutions, prospective students, Business to Business, seminars and trade shows.

Industry/Entity Type

Education

Font styles to use
Sans Serif

Colors
a54499

Requirements
Must have
• Consistent with our branding theme / colours.
• Template + content using information from our International Prospectus and web site.
• Delineation between domestic and international offerings.
• Showcasing the beautiful location from which we operate.
Nice to have
• Ability to utilise the presentation for generation of other marketing collateral (flyers, posters) in future.
• Cut in video footage of our location (Queensland, Brisbane, Gold Coast).
• Any general content / slides / video that may inspire travel to Australia to study or participation in study.
Should not have
• Be off-brand.

```html
<!DOCTYPE html>
<html lang="en">
<head>
<meta charset="utf-8">
<title>Juniper Learning and Skills Institute — Promotional Presentation</title>
<link href="https://fonts.googleapis.com/css2?family=Lato:wght@400;700;900&display=swap" rel="stylesheet">
<style>
:root{
  --purple:#a54499;
  --purple-deep:#6e2a6a;
  --ink:#1c1b1f;
  --charcoal:#2d2c31;
  --teal:#2c6c63;
  --teal-light:#3f8b80;
  --grey:#6a6a6e;
  --rule:#d9d6da;
  --paper:#ffffff;
}
*{box-sizing:border-box;margin:0;padding:0}
html,body{width:1200px;height:3600px;overflow:hidden;background:var(--paper)}
body{font-family:"Lato",Arial,sans-serif;color:var(--ink)}
.deck{display:grid;grid-template-columns:570px 570px;grid-auto-rows:320px;column-gap:20px;row-gap:40px;padding:20px}
.slide{position:relative;overflow:hidden;background:var(--paper);box-shadow:0 0 0 1px #e2e0e3}
.abs{position:absolute}
.photo{position:absolute;background:linear-gradient(135deg,#8d7f78,#c9b9a8)}
.photo.dark{background:linear-gradient(135deg,#1b1a20,#3b3640)}
.photo.warm{background:linear-gradient(135deg,#c9a45a,#e6d5a8)}
.photo.sky{background:linear-gradient(180deg,#7fb6dc,#3b8fb0 55%,#6d8f55)}
.photo.violet{background:linear-gradient(160deg,#2a1638,#7a3a8a 60%,#c07ab0)}
.photo.campus{background:linear-gradient(135deg,#9aa1a7,#d5d2cc)}
.photo.map{background:linear-gradient(135deg,#e9ecef,#d6dde3)}
.photo.city{background:linear-gradient(135deg,#3b3d44,#8c8f96)}
.brand{position:absolute;display:flex;align-items:center;gap:4px;font-weight:900;letter-spacing:.5px}
.brand-dot{width:7px;height:7px;border-radius:50%;background:var(--purple)}
.brand.top{top:10px;right:14px;font-size:12px;color:var(--ink)}
.footer{position:absolute;left:0;right:0;bottom:0;height:18px;background:var(--ink);color:#fff;font-size:6px;font-weight:700;letter-spacing:.6px;padding-left:14px;line-height:18px}
.footer .pg{position:absolute;right:14px;top:4px;width:10px;height:10px;background:var(--purple);font-size:5px;line-height:10px;text-align:center}
.title{font-weight:900;font-size:17px;letter-spacing:.3px}
.title .hl{color:var(--purple)}
.title-rule{width:26px;height:2px;background:var(--purple);margin-top:4px}
.txt{font-size:5.6px;line-height:1.55;color:var(--grey)}
.txt.w{color:#e6e3e8}
.lead{font-size:7px;line-height:1.4;color:var(--purple);font-weight:700}
.tile{position:absolute;color:#fff;padding:8px}
.tile h4{font-size:7px;font-weight:900;line-height:1.2;margin-bottom:4px}
.tile p{font-size:5px;line-height:1.5;color:#eadcec}
.bg-purple{background:var(--purple)}
.bg-deep{background:var(--purple-deep)}
.bg-ink{background:var(--charcoal)}
.bg-teal{background:var(--teal)}
.bg-teal2{background:var(--teal-light)}
/* agenda */
.agenda-row{position:absolute;left:120px;width:330px;height:24px;border:1px solid var(--rule);display:flex;align-items:center;font-size:7px;font-weight:700}
.agenda-row .num{width:28px;height:100%;display:flex;align-items:center;justify-content:center;border-right:1px solid var(--rule);color:var(--purple)}
.agenda-row .lbl{padding-left:10px}
.agenda-row.active{background:var(--ink);color:#fff;border-color:var(--ink)}
.agenda-row.active .num{color:#fff;border-color:#444}
/* values */
.value{position:absolute;top:60px;width:140px;text-align:center}
.value svg{display:block;margin:0 auto 4px}
.value h3{font-size:9px;font-weight:900;color:var(--purple);margin-bottom:3px}
/* lists */
.bullets{list-style:none;font-size:5.8px;color:var(--grey);line-height:1.9}
.bullets li::before{content:"";display:inline-block;width:3px;height:3px;border-radius:50%;background:var(--purple);margin-right:5px;vertical-align:middle}
.sub-h{font-size:6.5px;font-weight:900;color:var(--purple);margin:6px 0 2px}
/* reasons */
.reasons{list-style:none;text-align:center;color:#fff;font-weight:900;font-size:9px}
.reasons li{padding:5px 0;border-bottom:1px solid rgba(255,255,255,.35)}
/* course table */
.course-table{border-collapse:collapse;font-size:5px;width:250px}
.course-table th{background:var(--purple);color:#fff;text-align:left;padding:3px 4px;width:78px;font-weight:700;border-bottom:1px solid #fff}
.course-table td{padding:3px 4px;border-bottom:1px solid var(--rule);color:var(--grey)}
/* team */
.member{position:absolute;top:62px;width:110px;text-align:center}
.member .ring{width:84px;height:84px;border-radius:50%;margin:0 auto 8px;border:3px solid #f2f0f3;box-shadow:0 0 0 1px var(--rule)}
.member h4{font-size:9px;font-weight:900;color:var(--purple)}
.member .role{font-size:5px;color:var(--grey);letter-spacing:.5px;margin:2px 0 5px}
.member p{font-size:5px;color:var(--grey);line-height:1.5}
.socials{display:flex;gap:4px;justify-content:center;margin-top:5px}
.socials span{width:9px;height:9px;border-radius:50%;background:var(--charcoal)}
/* timeline */
.step{position:absolute;width:90px;font-size:6.5px;font-weight:700;color:var(--ink)}
.step b{display:block;font-size:15px;font-weight:400;color:var(--ink)}
.step.pu{color:var(--purple)}
.step.te{color:var(--teal)}
.step.pu b{color:var(--purple)}
.step.te b{color:var(--teal)}
/* contact */
.addr{font-size:5.5px;line-height:1.6;color:#dcd8de}
.addr h5{font-size:6.5px;color:var(--purple);font-weight:900;letter-spacing:.5px}
</style>
</head>
<body>
<main class="deck">

  <!-- 1 Opening -->
  <section class="slide">
    <div class="photo dark" style="inset:0" role="img" aria-label="Darkened photo of students in a classroom"></div>
    <div class="brand" style="left:0;right:0;top:92px;justify-content:center;color:#fff;font-size:40px;gap:10px"><span class="brand-dot" style="width:20px;height:20px"></span>JLSI</div>
    <div class="abs" style="left:0;right:0;top:146px;text-align:center;color:#fff;font-size:7px;letter-spacing:1.5px;font-weight:700">JUNIPER LEARNING AND SKILLS INSTITUTE</div>
    <div class="abs" style="left:195px;top:170px;width:180px;height:40px;border:1.5px solid var(--purple);text-align:center;color:#fff;padding-top:8px">
      <div style="font-size:11px;font-weight:900;letter-spacing:.5px">INTRODUCTION</div>
      <div style="font-size:6px;color:#d8d2da;margin-top:2px">Brisbane | Australia</div>
    </div>
  </section>

  <!-- 2 Agenda -->
  <section class="slide">
    <div class="brand top"><span class="brand-dot"></span>JLSI</div>
    <div class="abs" style="left:0;right:0;top:26px;text-align:center"><h2 class="title hl" style="color:var(--purple)">AGENDA</h2><div class="title-rule" style="margin:4px auto 0"></div></div>
    <div class="agenda-row active" style="top:68px"><span class="num">01</span><span class="lbl">LOREM IPSUM DOLOR SIT AMET</span></div>
    <div class="agenda-row" style="top:102px"><span class="num">02</span><span class="lbl">LOREM IPSUM DOLOR SIT AMET</span></div>
    <div class="agenda-row" style="top:136px"><span class="num">03</span><span class="lbl">LOREM IPSUM DOLOR SIT AMET</span></div>
    <div class="agenda-row" style="top:170px"><span class="num">04</span><span class="lbl">LOREM IPSUM DOLOR SIT AMET</span></div>
    <div class="agenda-row" style="top:204px"><span class="num">05</span><span class="lbl">LOREM IPSUM DOLOR SIT AMET</span></div>
    <div class="footer">JUNIPER LEARNING AND SKILLS INSTITUTE<span class="pg">2</span></div>
  </section>

  <!-- 3 CEO -->
  <section class="slide">
    <div class="abs" style="left:14px;top:22px;width:150px">
      <h2 class="title" style="font-size:14px">CEO <span class="hl">&amp;</span> WELCOME</h2>
      <div class="title-rule"></div>
      <p class="lead" style="margin-top:10px">It is an exciting time to be a student at Juniper Learning and Skills Institute and I invite you to join us.</p>
      <p class="txt" style="margin-top:8px">JLSI is home to people from all over the world who want practical skills, real support and a clear path into study, work and life in Australia.</p>
      <p class="txt" style="margin-top:6px">We focus on you as a person and help you build the confidence, language and skills you need to succeed in your chosen field and beyond.</p>
      <p class="txt" style="margin-top:6px">Our staff are caring, our classes are small and our campuses are friendly places to learn, meet new people and grow.</p>
    </div>
    <div class="photo warm" style="left:175px;top:0;width:205px;height:320px" role="img" aria-label="Portrait photo of the Chief Executive Officer"></div>
    <div class="abs bg-ink" style="left:380px;top:0;width:190px;height:320px;background:var(--ink)"></div>
    <div class="brand" style="left:380px;width:190px;top:100px;justify-content:center;color:#fff;font-size:18px"><span class="brand-dot" style="width:10px;height:10px"></span>JLSI</div>
    <p class="abs" style="left:398px;top:140px;width:160px;color:#fff;font-size:12px;font-weight:900;line-height:1.25">...turn dreams into reality and aspirations into achieved goals.</p>
    <p class="abs" style="left:398px;top:202px;width:160px;color:var(--purple);font-size:6px;font-weight:700">Mara Lindqvist, Chief Executive Officer</p>
    <div class="brand" style="right:14px;bottom:10px;color:#fff;font-size:9px"><span class="brand-dot" style="width:5px;height:5px"></span>JLSI</div>
    <div class="abs bg-purple" style="left:14px;bottom:10px;width:10px;height:10px"></div>
  </section>

  <!-- 4 Mission, Vision, Values -->
  <section class="slide">
    <div class="brand top"><span class="brand-dot"></span>JLSI</div>
    <div class="abs" style="left:0;right:0;top:22px;text-align:center"><h2 class="title">MISSION, VISION and VALUES</h2><div class="title-rule" style="margin:4px auto 0"></div></div>
    <div class="value" style="left:45px">
      <svg width="30" height="22" viewBox="0 0 30 22"><path d="M2 11 Q15 -2 28 11 Q15 24 2 11Z" fill="none" stroke="#a54499" stroke-width="2.5"/><circle cx="15" cy="11" r="4" fill="#a54499"/></svg>
      <h3>VISION</h3><p class="txt">Empowering people to become successful in the future and supporting our local community.</p>
    </div>
    <div class="value" style="left:215px">
      <svg width="26" height="26" viewBox="0 0 26 26"><circle cx="13" cy="13" r="11" fill="none" stroke="#a54499" stroke-width="2.5"/><circle cx="13" cy="13" r="6" fill="none" stroke="#a54499" stroke-width="2.5"/><circle cx="13" cy="13" r="2" fill="#a54499"/></svg>
      <h3>MISSION</h3><p class="txt">To equip all types of learners with practical skills, taught with care and inspiring experiences.</p>
    </div>
    <div class="value" style="left:385px">
      <svg width="26" height="24" viewBox="0 0 26 24"><path d="M13 22 L3 12 A6 6 0 0 1 13 4 A6 6 0 0 1 23 12Z" fill="#a54499"/></svg>
      <h3>VALUES</h3><p class="txt">Love, Caring, Serving, Collaborating</p>
    </div>
    <div class="photo campus" style="left:0;right:0;top:190px;height:112px" role="img" aria-label="Strip of photos showing students learning together"></div>
    <div class="footer">JUNIPER LEARNING AND SKILLS INSTITUTE<span class="pg">4</span></div>
  </section>

  <!-- 5 Why Choose (tiles) -->
  <section class="slide">
    <div class="brand top"><span class="brand-dot"></span>JLSI</div>
    <div class="abs" style="left:0;right:0;top:16px;text-align:center"><h2 class="title">Why Choose <span class="hl">JLSI</span></h2><div class="title-rule" style="margin:3px auto 0"></div></div>
    <div class="photo" style="left:20px;top:48px;width:106px;height:125px" role="img" aria-label="Students studying"></div>
    <div class="tile bg-deep" style="left:126px;top:48px;width:106px;height:125px"><h4>NATIONALLY RECOGNISED QUALIFICATIONS</h4><p>Courses built to national standards and respected by employers.</p></div>
    <div class="photo warm" style="left:232px;top:48px;width:106px;height:125px" role="img" aria-label="Graduates celebrating"></div>
    <div class="tile bg-ink" style="left:338px;top:48px;width:106px;height:125px"><h4>OUTCOME FOCUSED</h4><p>Learning that leads to real jobs and further study.</p></div>
    <div class="photo city" style="left:444px;top:48px;width:106px;height:125px" role="img" aria-label="Students in a group"></div>
    <div class="tile bg-ink" style="left:20px;top:173px;width:106px;height:125px"><h4>VISION BRINGS SUCCESS</h4><p>We help every student set clear goals and reach them.</p></div>
    <div class="photo campus" style="left:126px;top:173px;width:106px;height:125px" role="img" aria-label="Graduation certificates"></div>
    <div class="tile bg-purple" style="left:232px;top:173px;width:106px;height:125px"><h4>MULTI-LINGUAL STAFF</h4><p>Friendly staff who speak many languages.</p></div>
    <div class="photo warm" style="left:338px;top:173px;width:106px;height:125px" role="img" aria-label="Hands joined in a group"></div>
    <div class="tile bg-ink" style="left:444px;top:173px;width:106px;height:125px"><h4>CONVENIENT START DATES</h4><p>Start your course at many times through the year.</p></div>
    <div class="footer" style="height:14px;line-height:14px">JUNIPER LEARNING AND SKILLS INSTITUTE<span class="pg" style="top:2px">5</span></div>
  </section>

  <!-- 6 Why Choose (list) -->
  <section class="slide">
    <div class="brand top"><span class="brand-dot"></span>JLSI</div>
    <div class="abs" style="left:16px;top:18px;width:330px">
      <h2 class="title">Why Choose <span class="hl">JLSI</span></h2><div class="title-rule"></div>
      <p class="txt" style="margin-top:8px">JLSI's combination of modern learning facilities, great campus locations, experienced and passionate trainers, and small class sizes make it an ideal choice for students seeking an excellent education and training experience.</p>
      <ul class="bullets" style="margin-top:10px">
        <li>Nationally recognised qualifications</li><li>Outcome focused</li><li>Vision brings success</li><li>Recognition for prior learning and credit transfer</li><li>Multi-lingual staff</li><li>Convenient start dates</li><li>Small class sizes</li><li>Pathway to university</li>
      </ul>
      <p class="txt" style="margin-top:8px">Aliquam tempor elit, dapibus in viverra quis, feugiat a tellus. Phasellus viverra nulla ut metus varius laoreet. Quisque rutrum, donec imperdiet.</p>
    </div>
    <div class="photo" style="left:360px;top:0;width:210px;height:302px;background:linear-gradient(160deg,#e9e8ea,#b9b5bd)" role="img" aria-label="Photo of a smiling student holding a folder"></div>
    <div class="footer">JUNIPER LEARNING AND SKILLS INSTITUTE<span class="pg">6</span></div>
  </section>

  <!-- 7 Our Locations -->
  <section class="slide">
    <div class="abs" style="left:0;width:300px;top:30px;text-align:center"><h2 class="title">OUR <span class="hl">LOCATIONS</span></h2><div class="title-rule" style="margin:4px auto 0"></div><p class="txt" style="margin-top:4px">Two convenient campus locations with modern facilities</p></div>
    <div class="abs" style="left:16px;top:100px;width:270px">
      <p class="txt">Juniper Learning and Skills Institute (JLSI) offers two convenient campus locations with modern facilities.</p>
      <p class="txt" style="margin-top:6px">JLSI's City Campus is located in the heart of Brisbane's CBD, close to an amazing array of local restaurants, shopping, parks and public transport.</p>
      <p class="txt" style="margin-top:6px">JLSI's Parkview Campus is situated right next door to the bustling Bellhaven Rise shopping centre and is only minutes from the university, making it an easy trip for students from all over Brisbane and 15 minutes by bus from the CBD.</p>
    </div>
    <div class="photo map" style="left:300px;top:0;width:270px;height:302px" role="img" aria-label="Map of Brisbane showing the two campus locations"></div>
    <svg class="abs" style="left:390px;top:150px" width="22" height="30" viewBox="0 0 22 30"><path d="M11 29 C4 19 1 14 1 10 A10 10 0 0 1 21 10 C21 14 18 19 11 29Z" fill="#3b8fc8"/><circle cx="11" cy="10" r="4" fill="#fff"/></svg>
    <div class="abs" style="left:414px;top:156px;font-size:6px;font-weight:700">Bellhaven Rise</div>
    <div class="footer">JUNIPER LEARNING AND SKILLS INSTITUTE<span class="pg">7</span></div>
  </section>

  <!-- 8 Life in Brisbane -->
  <section class="slide">
    <div class="photo sky" style="left:0;top:0;width:570px;height:140px" role="img" aria-label="Photo of the Brisbane riverside beach and city skyline"></div>
    <div class="abs" style="left:0;right:0;top:148px;text-align:right;padding-right:20px"><h2 class="title">LIFE IN <span class="hl">BRISBANE</span></h2></div>
    <div class="abs" style="left:16px;top:172px;width:540px">
      <p class="txt" style="color:var(--ink);font-weight:700">Brisbane is the capital of Queensland, the Sunshine State, renowned for being beautiful one day and perfect the next. But it is much more than that. It is a city where the locals and students are friendly and accommodating, and where cultural diversity is not only encouraged, it is accepted and established way of life.</p>
    </div>
    <div class="abs" style="left:16px;top:202px;width:260px">
      <p class="txt">Brisbane is one of Australia's most modern cities, making it ideal for students wanting to enjoy city style shopping and top sporting facilities close to the golden beaches and clean air of country towns nearby.</p>
      <p class="txt" style="margin-top:5px">The vibrant Brisbane region is home to seasons, festivals, parks and markets, well known for great food, coffee and outdoor living all year round.</p>
    </div>
    <div class="abs" style="left:296px;top:202px;width:260px">
      <p class="txt">It's a safe city with an abundance of wildlife, sunshine, beaches and parks for visitors and residents to explore.</p>
      <p class="txt" style="margin-top:5px">As well as being a dynamic and attractive hub for the region, Brisbane boasts a great public transport system so getting around to study and work is easy.</p>
      <p class="txt" style="margin-top:5px">International students keep coming to Brisbane each year, and the city welcomes them with open arms.</p>
    </div>
    <div class="footer">JUNIPER LEARNING AND SKILLS INSTITUTE<span class="pg">8</span></div>
  </section>

  <!-- 9 Top reasons -->
  <section class="slide">
    <div class="photo violet" style="inset:0" role="img" aria-label="Night photo of Brisbane city lights with a purple overlay"></div>
    <h2 class="abs" style="left:60px;top:22px;width:220px;color:#fff;font-size:15px;font-weight:900;line-height:1.15">TOP REASONS WHY <span style="color:#e7a5dc">STUDENTS LOVE BRISBANE</span></h2>
    <ul class="reasons abs" style="left:150px;top:96px;width:270px">
      <li>Capital of Sunshine State</li><li>Affordable for students</li><li>New purpose-built student accommodation</li><li>Reliable public transport</li><li>A safe, welcoming city</li><li>Useful websites</li>
    </ul>
  </section>

  <!-- 10 Domestic courses -->
  <section class="slide">
    <div class="brand top"><span class="brand-dot"></span>JLSI</div>
    <h2 class="abs title" style="right:70px;top:12px"><span class="hl">DOMESTIC</span> COURSES</h2>
    <div class="abs bg-purple" style="left:16px;top:40px;width:538px;height:16px;color:#fff;font-size:7px;font-weight:900;line-height:16px;padding-left:8px">LNG-204 Certificate II in Spoken and Written English</div>
    <p class="abs" style="left:16px;top:62px;font-size:6px;font-weight:900">CRICOS CODE: 0000000</p>
    <p class="abs txt" style="left:16px;top:72px;width:538px">This certificate helps learners build the English they need for everyday life, further study and work in Australia, covering speaking, listening, reading and writing.</p>
    <table class="course-table abs" style="left:16px;top:100px">
      <tr><th>COURSE DURATION</th><td>20 weeks including 2 weeks of holidays</td></tr>
      <tr><th>CAMPUS</th><td>City Campus, Bellhaven Rise campus</td></tr>
      <tr><th>MODE OF STUDY</th><td>Face to face, full-time</td></tr>
      <tr><th>ENTRY REQUIREMENTS</th><td>No entry requirements</td></tr>
      <tr><th>INTAKE DATES</th><td>Jan 9, Feb 6, Mar 6, Apr 3, May 1, Jun 5</td></tr>
      <tr><th>ASSESSMENT METHOD</th><td>Assessment tasks and class activities</td></tr>
      <tr><th>COST</th><td>Fees available on enquiry</td></tr>
      <tr><th>COURSE STRUCTURE</th><td>Total number of units: 7</td></tr>
    </table>
    <div class="abs" style="left:300px;top:100px;width:254px">
      <p style="font-size:6px;font-weight:900">Course units</p>
      <ul class="bullets" style="margin-top:3px;line-height:1.7;font-size:5.3px">
        <li>Give spoken information in a familiar context</li><li>Participate in short conversations</li><li>Read short everyday texts</li><li>Write short notes and messages</li><li>Complete simple forms and documents</li><li>Use listening skills in daily life</li><li>Plan a learning pathway</li>
      </ul>
    </div>
    <div class="footer">JUNIPER LEARNING AND SKILLS INSTITUTE<span class="pg">10</span></div>
  </section>

  <!-- 11 Live on campus -->
  <section class="slide">
    <div class="photo campus" style="left:0;top:0;width:225px;height:302px" role="img" aria-label="Photo of a student studying in a campus lounge"></div>
    <div class="abs" style="left:245px;top:22px;width:300px">
      <h2 class="title">LIVE <span class="hl">ON CAMPUS</span></h2><div class="title-rule"></div>
      <p class="txt" style="margin-top:8px">Our friendly Student Services team are here to help you settle in to college life, delivering orientation, study skills and English development workshops, individual assistance, counselling services as well as fun student activities throughout the year.</p>
      <p class="sub-h">CAMPUS FACILITIES:</p>
      <ul class="bullets"><li>Technology</li><li>Student Lounge</li></ul>
      <p class="sub-h">STUDENT SERVICES</p>
      <ul class="bullets"><li>Orientation</li><li>Student Support Services</li></ul>
      <p style="font-size:6.5px;font-weight:700;color:var(--purple);margin-top:10px">Staff are here to help you settle into college life</p>
    </div>
    <div class="footer">JUNIPER LEARNING AND SKILLS INSTITUTE<span class="pg">11</span></div>
  </section>

  <!-- 12 Student services (tiles) -->
  <section class="slide">
    <div class="brand top"><span class="brand-dot"></span>JLSI</div>
    <div class="abs" style="left:0;right:0;top:18px;text-align:center"><h2 class="title"><span class="hl">STUDENT</span> SERVICES</h2></div>
    <p class="abs txt" style="left:60px;top:42px;width:450px;text-align:center">Lorem ipsum dolor sit amet, consectetuer adipiscing elit. Aenean commodo ligula eget dolor. Aenean massa. Cum sociis natoque penatibus et magnis dis parturient montes. Donec quam felis, ultricies nec.</p>
    <div class="tile bg-ink" style="left:16px;top:78px;width:179px;height:110px"><h4>Lorem ipsum dolor</h4><p>Lorem ipsum dolor sit amet, consectetuer adipiscing elit. Aenean commodo ligula eget dolor. Aenean massa.</p></div>
    <div class="tile bg-ink" style="left:195px;top:78px;width:179px;height:110px;background:#3a3940"><h4>Lorem ipsum dolor</h4><p>Lorem ipsum dolor sit amet, consectetuer adipiscing elit. Aenean commodo ligula eget dolor. Aenean massa.</p></div>
    <div class="tile bg-deep" style="left:374px;top:78px;width:180px;height:110px"><h4>Lorem ipsum dolor</h4><p>Lorem ipsum dolor sit amet, consectetuer adipiscing elit. Aenean commodo ligula eget dolor. Aenean massa.</p></div>
    <div class="tile bg-purple" style="left:16px;top:188px;width:179px;height:110px"><h4>Lorem ipsum dolor</h4><p>Lorem ipsum dolor sit amet, consectetuer adipiscing elit. Aenean commodo ligula eget dolor. Aenean massa.</p></div>
    <div class="tile bg-ink" style="left:195px;top:188px;width:179px;height:110px"><h4>Lorem ipsum dolor</h4><p>Lorem ipsum dolor sit amet, consectetuer adipiscing elit. Aenean commodo ligula eget dolor. Aenean massa.</p></div>
    <div class="tile bg-deep" style="left:374px;top:188px;width:180px;height:110px"><h4>Lorem ipsum dolor</h4><p>Lorem ipsum dolor sit amet, consectetuer adipiscing elit. Aenean commodo ligula eget dolor. Aenean massa.</p></div>
    <div class="footer" style="height:14px;line-height:14px">JUNIPER LEARNING AND SKILLS INSTITUTE<span class="pg" style="top:2px">12</span></div>
  </section>

  <!-- 13 Student services (icons) -->
  <section class="slide">
    <div class="brand top"><span class="brand-dot"></span>JLSI</div>
    <div class="abs" style="left:0;right:0;top:18px;text-align:center"><h2 class="title"><span class="hl">STUDENT</span> SERVICES</h2></div>
    <p class="abs txt" style="left:60px;top:42px;width:450px;text-align:center">Lorem ipsum dolor sit amet, consectetuer adipiscing elit. Aenean commodo ligula eget dolor. Aenean massa. Cum sociis natoque penatibus et magnis dis parturient montes. Donec quam felis, ultricies nec.</p>
    <div class="tile bg-teal" style="left:16px;top:80px;width:107px;height:220px;text-align:center;padding-top:18px">
      <svg width="26" height="22" viewBox="0 0 26 22"><rect x="2" y="12" width="4" height="8" fill="#fff"/><rect x="9" y="7" width="4" height="13" fill="#fff"/><rect x="16" y="3" width="4" height="17" fill="#fff"/><rect x="0" y="20" width="26" height="1.5" fill="#fff"/></svg>
      <h4 style="margin-top:26px">Lorem ipsum dolor sit amet</h4><p>Lorem ipsum dolor sit amet, consectetuer adipiscing elit.</p></div>
    <div class="tile bg-teal2" style="left:123px;top:80px;width:107px;height:220px;text-align:center;padding-top:18px">
      <svg width="22" height="24" viewBox="0 0 22 24"><path d="M11 1 L21 5 V12 C21 18 16 22 11 23 C6 22 1 18 1 12 V5Z" fill="#fff"/></svg>
      <h4 style="margin-top:24px">Lorem ipsum dolor sit amet</h4><p>Lorem ipsum dolor sit amet, consectetuer adipiscing elit.</p></div>
    <div class="tile bg-ink" style="left:230px;top:80px;width:107px;height:220px;text-align:center;padding-top:18px">
      <svg width="24" height="24" viewBox="0 0 24 24"><circle cx="12" cy="12" r="7" fill="none" stroke="#fff" stroke-width="4" stroke-dasharray="3 2.5"/><circle cx="12" cy="12" r="3" fill="#fff"/></svg>
      <h4 style="margin-top:24px">Lorem ipsum dolor sit amet</h4><p>Lorem ipsum dolor sit amet, consectetuer adipiscing elit.</p></div>
    <div class="tile bg-deep" style="left:337px;top:80px;width:108px;height:220px;text-align:center;padding-top:18px">
      <svg width="26" height="22" viewBox="0 0 26 22"><path d="M1 21 V10 L8 6 V10 L15 6 V10 L22 6 V21Z M19 6 V1 H23 V8" fill="#fff"/></svg>
      <h4 style="margin-top:26px">Lorem ipsum dolor sit amet</h4><p>Lorem ipsum dolor sit amet, consectetuer adipiscing elit.</p></div>
    <div class="tile bg-purple" style="left:445px;top:80px;width:109px;height:220px;text-align:center;padding-top:18px">
      <svg width="24" height="24" viewBox="0 0 24 24"><rect x="2" y="4" width="20" height="18" rx="2" fill="none" stroke="#fff" stroke-width="2.5"/><rect x="2" y="4" width="20" height="5" fill="#fff"/><rect x="6" y="1" width="2.5" height="5" fill="#fff"/><rect x="15.5" y="1" width="2.5" height="5" fill="#fff"/></svg>
      <h4 style="margin-top:24px">Lorem ipsum dolor sit amet</h4><p>Lorem ipsum dolor sit amet, consectetuer adipiscing elit.</p></div>
    <div class="footer" style="height:14px;line-height:14px">JUNIPER LEARNING AND SKILLS INSTITUTE<span class="pg" style="top:2px">13</span></div>
  </section>

  <!-- 14 Student services (photo grid) -->
  <section class="slide">
    <div class="brand top"><span class="brand-dot"></span>JLSI</div>
    <h2 class="abs title" style="right:70px;top:16px"><span class="hl">STUDENT</span> SERVICES</h2>
    <div class="abs" style="left:16px;top:60px;width:170px">
      <p class="txt">Lorem ipsum dolor sit amet, consectetuer adipiscing elit. Aenean commodo ligula eget dolor. Aenean massa. Cum sociis natoque penatibus et magnis dis parturient montes, nascetur ridiculus mus. Donec quam felis, ultricies nec, pellentesque eu, pretium quis, sem. Nulla consequat massa quis enim. Donec pede justo, fringilla vel, aliquet nec, vulputate eget, arcu.</p>
      <p class="txt" style="margin-top:6px">In enim justo, rhoncus ut, imperdiet a, venenatis vitae, justo. Nullam dictum felis eu pede mollis pretium. Integer tincidunt. Cras dapibus. Vivamus elementum semper nisi. Aenean vulputate eleifend tellus.</p>
    </div>
    <div class="photo" style="left:200px;top:48px;width:120px;height:125px" role="img" aria-label="Students reading together"></div>
    <div class="tile bg-purple" style="left:320px;top:48px;width:120px;height:125px"><h4>Lorem ipsum dolor sit amet</h4><p>Lorem ipsum dolor sit amet, consectetuer adipiscing elit.</p></div>
    <div class="photo warm" style="left:440px;top:48px;width:114px;height:125px" role="img" aria-label="Student smiling in class"></div>
    <div class="tile bg-deep" style="left:200px;top:173px;width:120px;height:125px"><h4>Lorem ipsum dolor sit amet</h4><p>Lorem ipsum dolor sit amet, consectetuer adipiscing elit.</p></div>
    <div class="photo campus" style="left:320px;top:173px;width:120px;height:125px" role="img" aria-label="Graduation scroll"></div>
    <div class="tile bg-purple" style="left:440px;top:173px;width:114px;height:125px"><h4>Lorem ipsum dolor sit amet</h4><p>Lorem ipsum dolor sit amet, consectetuer adipiscing elit.</p></div>
    <div class="footer" style="height:14px;line-height:14px">JUNIPER LEARNING AND SKILLS INSTITUTE<span class="pg" style="top:2px">14</span></div>
  </section>

  <!-- 15 Our team -->
  <section class="slide">
    <div class="brand top"><span class="brand-dot"></span>JLSI</div>
    <div class="abs" style="left:0;right:0;top:22px;text-align:center"><h2 class="title">OUR <span class="hl">TEAM</span></h2><div class="title-rule" style="margin:4px auto 0"></div></div>
    <div class="member" style="left:30px"><div class="ring photo campus" style="position:relative" role="img" aria-label="Team member portrait"></div><h4>Lorem ipsum</h4><div class="role">LOREM IPSUM DOLOR</div><p>Lorem ipsum dolor sit amet, consectetuer adipiscing elit.</p><div class="socials"><span></span><span></span><span></span></div></div>
    <div class="member" style="left:160px"><div class="ring photo warm" style="position:relative" role="img" aria-label="Team member portrait"></div><h4>Lorem ipsum</h4><div class="role">LOREM IPSUM DOLOR</div><p>Lorem ipsum dolor sit amet, consectetuer adipiscing elit.</p><div class="socials"><span></span><span></span><span></span></div></div>
    <div class="member" style="left:290px"><div class="ring photo" style="position:relative" role="img" aria-label="Team member portrait"></div><h4>Lorem ipsum</h4><div class="role">LOREM IPSUM DOLOR</div><p>Lorem ipsum dolor sit amet, consectetuer adipiscing elit.</p><div class="socials"><span></span><span></span><span></span></div></div>
    <div class="member" style="left:420px"><div class="ring photo city" style="position:relative" role="img" aria-label="Team member portrait"></div><h4>Lorem ipsum</h4><div class="role">LOREM IPSUM DOLOR</div><p>Lorem ipsum dolor sit amet, consectetuer adipiscing elit.</p><div class="socials"><span></span><span></span><span></span></div></div>
    <div class="footer">JUNIPER LEARNING AND SKILLS INSTITUTE<span class="pg">15</span></div>
  </section>

  <!-- 16 Statement -->
  <section class="slide">
    <div class="photo city" style="inset:0;background:linear-gradient(135deg,#26262b,#55565c 60%,#34343a)" role="img" aria-label="Darkened photo of hands writing at a desk"></div>
    <p class="abs" style="left:34px;top:34px;width:230px;color:#fff;font-size:13px;font-weight:900;line-height:1.25">Lorem ipsum dolor sit amet, consectetuer adipiscing elit. Aenean commodo ligula eget dolor.</p>
    <div class="brand" style="left:150px;top:160px;color:#fff;font-size:26px;gap:8px"><span class="brand-dot" style="width:14px;height:14px"></span>JLSI</div>
    <div class="abs" style="right:16px;bottom:10px;color:#ccc;font-size:6px">16</div>
  </section>

  <!-- 17 How to apply -->
  <section class="slide">
    <div class="brand top"><span class="brand-dot"></span>JLSI</div>
    <div class="abs" style="left:0;right:0;top:22px;text-align:center"><h2 class="title">HOW <span class="hl">TO APPLY</span></h2></div>
    <p class="abs txt" style="left:60px;top:46px;width:450px;text-align:center">Lorem ipsum dolor sit amet, consectetuer adipiscing elit. Aenean commodo ligula eget dolor. Aenean massa. Cum sociis natoque penatibus et magnis dis parturient montes. Donec quam felis, ultricies nec.</p>
    <svg class="abs" style="left:40px;top:160px" width="490" height="24" viewBox="0 0 490 24">
      <rect x="0" y="4" width="80" height="16" rx="8" fill="#6e2a6a"/>
      <rect x="70" y="4" width="90" height="16" fill="#a54499"/>
      <rect x="160" y="4" width="90" height="16" fill="#c98ac1"/>
      <rect x="250" y="4" width="80" height="16" fill="#3f8b80"/>
      <rect x="330" y="4" width="80" height="16" fill="#2c6c63"/>
      <rect x="400" y="4" width="90" height="16" rx="8" fill="#2d2c31"/>
      <g fill="#fff" stroke="#d9d6da"><circle cx="55" cy="12" r="8"/><circle cx="130" cy="12" r="8"/><circle cx="205" cy="12" r="8"/><circle cx="285" cy="12" r="8"/><circle cx="365" cy="12" r="8"/><circle cx="440" cy="12" r="8"/></g>
    </svg>
    <div class="step" style="left:80px;top:100px"><b>01</b>Complete application form</div>
    <div class="step pu" style="left:230px;top:100px"><b>03</b>Accept offer</div>
    <div class="step" style="left:390px;top:100px"><b>05</b>plan your arrival</div>
    <div class="step pu" style="left:150px;top:194px"><b>02</b>Submit application form to JLSI</div>
    <div class="step te" style="left:310px;top:194px"><b>04</b>Apply for a visa</div>
    <div class="step" style="left:465px;top:194px"><b>06</b>commence your studies</div>
    <div class="footer">JUNIPER LEARNING AND SKILLS INSTITUTE<span class="pg">17</span></div>
  </section>

  <!-- 18 Steps -->
  <section class="slide">
    <div class="brand top"><span class="brand-dot"></span>JLSI</div>
    <div class="abs" style="left:16px;top:18px;width:330px"><h2 class="title"><span class="hl">LOREM</span> IPSUM DOLOR SIT AMET</h2>
    <p class="txt" style="margin-top:4px">Lorem ipsum dolor sit amet, consectetuer adipiscing elit. Aenean commodo ligula eget dolor. Aenean massa. Cum sociis natoque penatibus et magnis dis parturient montes.</p></div>
    <div class="abs" style="left:16px;top:96px;width:230px">
      <p style="font-size:7px;font-weight:900;color:var(--purple)">01 LOREM <span class="txt" style="font-weight:400">Lorem ipsum dolor sit amet, consectetuer adipiscing elit. Aenean commodo.</span></p>
      <p style="font-size:7px;font-weight:900;color:var(--purple);margin-top:14px">02 LOREM <span class="txt" style="font-weight:400">Lorem ipsum dolor sit amet, consectetuer adipiscing elit. Aenean commodo.</span></p>
      <p style="font-size:7px;font-weight:900;color:var(--purple);margin-top:14px">03 LOREM <span class="txt" style="font-weight:400">Lorem ipsum dolor sit amet, consectetuer adipiscing elit. Aenean commodo.</span></p>
      <p style="font-size:7px;font-weight:900;color:var(--purple);margin-top:14px">04 LOREM <span class="txt" style="font-weight:400">Lorem ipsum dolor sit amet, consectetuer adipiscing elit. Aenean commodo.</span></p>
      <p class="txt" style="margin-top:14px">Nulla dapibus in viverra quis, feugiat a tellus. Phasellus viverra nulla ut metus varius laoreet. Quisque rutrum.</p>
    </div>
    <svg class="abs" style="left:300px;top:40px" width="260" height="262" viewBox="0 0 260 262">
      <polygon points="130,0 190,40 190,62 70,62 70,40" fill="#2d2c31"/>
      <rect x="70" y="62" width="120" height="8" fill="#1c1b1f"/>
      <rect x="50" y="76" width="170" height="42" fill="#2d2c31"/>
      <rect x="35" y="124" width="200" height="42" fill="#2c6c63"/>
      <rect x="20" y="172" width="220" height="42" fill="#6e2a6a"/>
      <rect x="5" y="220" width="250" height="42" fill="#a54499"/>
      <g fill="#fff" font-family="Lato, sans-serif" font-size="9" font-weight="900">
        <text x="64" y="101">04 LOREM</text><text x="49" y="149">03 LOREM</text><text x="34" y="197">02 LOREM</text><text x="19" y="245">01 LOREM</text>
      </g>
      <g fill="#e8dde8" font-family="Lato, sans-serif" font-size="5">
        <text x="140" y="101">Lorem ipsum dolor</text><text x="140" y="149">Lorem ipsum dolor</text><text x="140" y="197">Lorem ipsum dolor</text><text x="140" y="245">Lorem ipsum dolor</text>
      </g>
    </svg>
  </section>

  <!-- 19 Closing -->
  <section class="slide">
    <div class="photo" style="left:0;top:0;width:570px;height:250px;background:linear-gradient(90deg,#8a8f96,#c8c6c2 50%,#6d6d74)" role="img" aria-label="Photo of two smiling students on campus"></div>
    <div class="abs" style="left:185px;top:120px;width:200px;height:100px;background:rgba(28,27,31,.55)"></div>
    <div class="brand" style="left:185px;width:200px;top:138px;justify-content:center;color:#fff;font-size:26px;gap:8px"><span class="brand-dot" style="width:13px;height:13px"></span>JLSI</div>
    <div class="abs" style="left:185px;width:200px;top:180px;text-align:center;color:#fff;font-size:6px;font-weight:700;letter-spacing:.8px">JUNIPER LEARNING AND SKILLS INSTITUTE</div>
    <div class="abs" style="left:0;right:0;top:250px;height:70px;background:var(--ink)"></div>
    <div class="abs addr" style="left:16px;top:258px;width:150px"><h5>PARKVIEW CAMPUS</h5>+61 7 5550 0182<br>12 Marlow Road<br>Bellhaven Rise QLD 4122</div>
    <div class="abs addr" style="right:16px;top:258px;width:150px;text-align:right"><h5>CITY CAMPUS</h5>+61 7 5550 0347<br>Level 5, 88 Ashby Street<br>Brisbane QLD 4000</div>
    <div class="abs bg-purple" style="left:185px;top:286px;width:200px;height:20px;color:#fff;text-align:center;font-size:9px;font-weight:900;line-height:20px">www.jlsi-example.edu.au</div>
  </section>

  <!-- 20 Contact -->
  <section class="slide">
    <div class="abs" style="left:0;top:0;width:230px;height:320px;background:var(--ink)"></div>
    <div class="brand" style="left:20px;top:24px;color:#fff;font-size:22px;gap:7px"><span class="brand-dot" style="width:11px;height:11px"></span>JLSI</div>
    <div class="abs" style="left:20px;top:56px;color:#fff;font-size:6.5px;font-weight:900;letter-spacing:.6px">JUNIPER LEARNING AND SKILLS INSTITUTE</div>
    <div class="abs bg-purple" style="left:20px;top:72px;width:190px;height:18px;color:#fff;font-size:8px;font-weight:900;line-height:18px;padding-left:8px">www.jlsi-example.edu.au</div>
    <div class="abs addr" style="left:20px;top:104px;width:190px"><h5>PARKVIEW CAMPUS</h5>+61 7 5550 0182<br>info@jlsi-example.edu.au<br>12 Marlow Road<br>Bellhaven Rise QLD 4122</div>
    <div class="abs addr" style="left:20px;top:170px;width:190px"><h5>CITY CAMPUS</h5>+61 7 5550 0347<br>city@jlsi-example.edu.au<br>Level 5, 88 Ashby Street<br>Brisbane QLD 4000</div>
    <div class="abs" style="left:20px;top:268px;display:flex;gap:12px"><span style="width:12px;height:12px;border-radius:50%;background:#fff"></span><span style="width:12px;height:12px;border-radius:50%;background:#fff"></span><span style="width:12px;height:12px;border-radius:50%;background:#fff"></span><span style="width:12px;height:12px;border-radius:50%;background:#fff"></span><span style="width:12px;height:12px;border-radius:50%;background:#fff"></span></div>
    <div class="photo map" style="left:230px;top:0;width:340px;height:320px;background:linear-gradient(135deg,#f1f2f3,#d9dcdf)" role="img" aria-label="Street map of Brisbane with both campuses marked"></div>
    <svg class="abs" style="left:425px;top:88px" width="24" height="32" viewBox="0 0 24 32"><path d="M12 31 C4 20 1 15 1 11 A11 11 0 0 1 23 11 C23 15 20 20 12 31Z" fill="#a54499"/><circle cx="12" cy="11" r="4.5" fill="#fff"/></svg>
    <svg class="abs" style="left:432px;top:200px" width="24" height="32" viewBox="0 0 24 32"><path d="M12 31 C4 20 1 15 1 11 A11 11 0 0 1 23 11 C23 15 20 20 12 31Z" fill="#a54499"/><circle cx="12" cy="11" r="4.5" fill="#fff"/></svg>
  </section>

</main>
</body>
</html>
```